'Copper Kettle' needs a Facebook Design (timeline cover & profile pic +) Logo provided.

Copper Kettle - Stitched Sweetness is a new small business selling handmade children's clothing and other hand crafted home decor items for the nursery etc; all made by me.
I need a Facebook design which communicates professionalism and good quality and which reflects the target age range (0-6 years) without being 'childish'. Facebook is the main selling platform and so I need a coherent look which can be carried on to 'thank you for your purchase' cards / business cards. Colour wise, I wondered about either a simple brown kraft design, OR a very colourful, cheerful scheme. However, I am open to ideas if you have a good vision for the site. The only stipulation is that the colours / design must appeal to parents of girls AND boys please. Have added some images I like the style of.

Target Market(s)

Parents of 0-6 year old girls and boys. People looking to buy presents for 0-6 year olds.

Industry/Entity Type

Small Business

Requirements
Must have
• A coherent design
• A strong brand
• The logo (attached), a cover photo and a profile picture.
Nice to have
• Either a very colourful design (in a high quality way)
• Or a very simple understated design e.g. brown kraft / neutrals (but not boring)
Should not have
• any 'tackiness'
• should not be too 'childish' - more high-quality child like

```html
<!DOCTYPE html>
<html lang="en">
<head>
<meta charset="utf-8">
<title>Copper Kettle – Facebook Cover</title>
<link rel="stylesheet" href="https://fonts.googleapis.com/css2?family=Josefin+Sans:wght@100&family=Courier+Prime:wght@700&display=swap">
<style>
  :root {
    --kraft-deep: #2f221a;
    --kraft-dark: #3d2c21;
    --kraft-mid: #57412f;
    --kraft-light: #6b533f;
    --kraft-glow: rgba(120, 95, 75, 0.55);
    --kraft-shade: rgba(25, 16, 10, 0.45);
    --ink-white: #ffffff;
    --ornament-glow: rgba(235, 225, 215, 0.28);
    --profile-fill: #b3b3b3;
  }
  html, body {
    margin: 0;
    padding: 0;
    width: 1200px;
    height: 444px;
    overflow: hidden;
    background: var(--kraft-dark);
  }
  .cover {
    position: relative;
    width: 1200px;
    height: 444px;
    overflow: hidden;
    background:
      radial-gradient(ellipse 420px 260px at 22% 30%, var(--kraft-glow), transparent 70%),
      radial-gradient(ellipse 380px 220px at 70% 20%, var(--kraft-glow), transparent 70%),
      radial-gradient(ellipse 300px 200px at 55% 75%, var(--kraft-shade), transparent 70%),
      radial-gradient(ellipse 260px 300px at 8% 70%, var(--kraft-shade), transparent 70%),
      radial-gradient(ellipse 320px 240px at 92% 60%, var(--kraft-shade), transparent 70%),
      radial-gradient(ellipse 500px 200px at 38% 55%, rgba(110, 85, 65, 0.35), transparent 70%),
      linear-gradient(165deg, var(--kraft-mid) 0%, var(--kraft-light) 35%, var(--kraft-mid) 65%, var(--kraft-deep) 100%);
  }
  .kraft-texture {
    position: absolute;
    inset: 0;
    background:
      linear-gradient(118deg, transparent 40%, rgba(255,255,255,0.05) 41%, transparent 44%),
      linear-gradient(62deg, transparent 55%, rgba(0,0,0,0.10) 56%, transparent 60%),
      linear-gradient(150deg, transparent 20%, rgba(0,0,0,0.08) 21%, transparent 25%),
      linear-gradient(35deg, transparent 70%, rgba(255,255,255,0.04) 71%, transparent 75%);
  }
  .ornament {
    position: absolute;
    border-radius: 50%;
    background: radial-gradient(circle, var(--ornament-glow) 0%, transparent 70%);
  }
  .brand {
    position: absolute;
    left: 0;
    width: 1182px;
    top: 168px;
    text-align: center;
    color: var(--ink-white);
  }
  .brand-name {
    margin: 0;
    font-family: "Josefin Sans", sans-serif;
    font-weight: 100;
    font-size: 78px;
    letter-spacing: 6px;
    line-height: 1;
    text-transform: uppercase;
  }
  .brand-tagline {
    margin: 36px 0 0;
    font-family: "Courier Prime", monospace;
    font-weight: 700;
    font-size: 22px;
    letter-spacing: 4px;
    line-height: 1;
  }
  .profile-frame {
    position: absolute;
    left: 47px;
    top: 338px;
    width: 219px;
    height: 120px;
    background: var(--profile-fill);
    border: 4px solid var(--ink-white);
  }
</style>
</head>
<body>
  <main class="cover">
    <div class="kraft-texture" role="img" aria-label="Crumpled brown kraft paper background"></div>

    <div class="ornament" role="img" aria-label="Hanging glitter star ornament" style="left:42px;top:146px;width:80px;height:80px"></div>
    <div class="ornament" role="img" aria-label="Hanging glitter star ornament" style="left:180px;top:263px;width:66px;height:66px"></div>
    <div class="ornament" role="img" aria-label="Hanging glitter star ornament" style="left:286px;top:104px;width:66px;height:66px"></div>
    <div class="ornament" role="img" aria-label="Hanging glitter star ornament" style="left:820px;top:311px;width:78px;height:78px"></div>
    <div class="ornament" role="img" aria-label="Hanging glitter star ornament" style="left:902px;top:104px;width:66px;height:66px"></div>
    <div class="ornament" role="img" aria-label="Hanging glitter star ornament" style="left:1013px;top:166px;width:66px;height:66px"></div>
    <div class="ornament" role="img" aria-label="Hanging glitter star ornament" style="left:1106px;top:62px;width:80px;height:80px"></div>

    <header class="brand">
      <h1 class="brand-name">Copper Kettle</h1>
      <p class="brand-tagline">stitched sweetness</p>
    </header>

    <div class="profile-frame" role="img" aria-label="Profile picture area"></div>
  </main>
</body>
</html>
```